Property development company needs a name card design

I started my company since 2010, based in Auckland, New Zealand. We have been doing residential property rentals, individual low-rise residential property construction, small to medium scale residential development project. We will be participate in property investment as well. I have no favor of any specific design or color, just be creative and do anything you think will match the concept.

```html
<!DOCTYPE html>
<html lang="en">
<head>
<meta charset="UTF-8">
<title>Kauri Ridge – Name Card</title>
<link href="https://fonts.googleapis.com/css2?family=Quicksand:wght@400;500;600&display=swap" rel="stylesheet">
<style>
  :root {
    --backdrop: #ececec;
    --charcoal: #353535;
    --charcoal-deep: #2a2a2a;
    --charcoal-soft: #444444;
    --gold: #d0aa68;
    --gold-light: #d9b97f;
    --ink: #333333;
    --ink-muted: #5a5a5a;
    --white: #ffffff;
  }
  html, body {
    margin: 0;
    padding: 0;
    width: 1100px;
    height: 1200px;
    overflow: hidden;
    background: var(--backdrop);
    font-family: "Quicksand", sans-serif;
  }
  .name-card {
    position: absolute;
    left: 285px;
    top: 112px;
    width: 533px;
    height: 980px;
    background: var(--charcoal);
    overflow: hidden;
  }
  .card-shapes {
    position: absolute;
    inset: 0;
  }
  .company-name {
    position: absolute;
    left: 60px;
    width: 412px;
    top: 238px;
    text-align: center;
    color: var(--ink);
    font-weight: 600;
    margin: 0;
  }
  .company-name .main {
    display: block;
    font-size: 34px;
    letter-spacing: 12px;
    padding-left: 12px;
    line-height: 1;
  }
  .company-name .sub {
    display: block;
    margin-top: 10px;
    font-size: 15.5px;
    letter-spacing: 0.2px;
  }
  .person {
    position: absolute;
    right: 33px;
    top: 656px;
    text-align: right;
    color: var(--white);
  }
  .person-name {
    margin: 0;
    font-size: 46px;
    font-weight: 500;
    letter-spacing: -1px;
    line-height: 1;
  }
  .person-divider {
    width: 328px;
    height: 6px;
    margin: 14px 0 8px auto;
    background-image: radial-gradient(circle, var(--gold) 2.6px, transparent 3px);
    background-size: 11.4px 6px;
  }
  .person-role {
    margin: 0;
    font-size: 36px;
    font-weight: 400;
    letter-spacing: 2px;
    line-height: 1;
  }
  .website {
    position: absolute;
    left: 0;
    right: 0;
    bottom: 24px;
    text-align: center;
    color: var(--ink-muted);
    font-size: 27px;
    font-weight: 500;
    letter-spacing: 4px;
    margin: 0;
  }
</style>
</head>
<body>
  <div class="name-card">
    <svg class="card-shapes" width="533" height="980" viewBox="0 0 533 980" aria-hidden="true">
      <polygon points="533,0 533,980 260,980" fill="var(--charcoal-deep)" opacity="0.55"/>
      <polygon points="505,375 533,340 533,860 380,980 330,980" fill="var(--charcoal-deep)" opacity="0.7"/>
      <polygon points="0,740 0,980 200,980" fill="var(--charcoal-soft)" opacity="0.6"/>
      <polygon points="225,420 240,420 15,740 0,740" fill="var(--charcoal-deep)" opacity="0.8"/>
      <polygon points="60,0 472,0 472,338 266,438 60,338" fill="var(--gold)"/>
      <path d="M0,880 Q266,820 533,880 L533,980 L0,980 Z" fill="var(--gold-light)"/>
    </svg>
    <h1 class="company-name">
      <span class="main">KAURI RIDGE</span>
      <span class="sub">INVESTMENT &amp; DEVELOPMENT LTD</span>
    </h1>
    <div class="person">
      <p class="person-name">MARA LINDQVIST</p>
      <div class="person-divider"></div>
      <p class="person-role">Director</p>
    </div>
    <p class="website">WWW.YOURSITE.COM</p>
  </div>
</body>
</html>
```